Informational Business Handout needs Company Information

We have this informational handout that we would like to start handing out to clients; however, the original designer failed to include any of our company contact information. Our main request is that you redesign this card with the appropriate contact information as listed below. We would like the information/content that is currently on the card to be on the new design as well. Feel free to take liberty with the rest of the card design, or not. Please see the card specifications and our company contact information below.

Card details: 7 x 5 inches (17.78 x 12.5 cm). Cardstock.

Company Contact Details:
Dorian Maskell, JD
TrueMark, PLLC
538 E. Harlow Ave, Ste. 410, St. George, UT 84913
hello@truemark-example.com
(435) 555-0172

```html
<!DOCTYPE html>
<html lang="en">
<head>
<meta charset="utf-8">
<title>Special Needs Trust Handout</title>
<link rel="stylesheet" href="https://fonts.googleapis.com/css2?family=Poppins:wght@400;500;600&display=swap">
<style>
  :root {
    --rust: #a44a28;
    --navy: #1b2352;
    --backdrop: #cfcfcf;
    --paper: #ffffff;
    --rule: #c9c9c9;
    --photo-orange: #c8701f;
    --photo-blue: #8fb2e6;
    --photo-steel: #6d7ea6;
  }
  * { margin: 0; padding: 0; box-sizing: border-box; }
  html, body { width: 1200px; height: 733px; overflow: hidden; }
  body {
    background: var(--backdrop);
    font-family: "Poppins", sans-serif;
    color: var(--navy);
    position: relative;
  }
  .card {
    position: absolute;
    top: 208px;
    width: 443px;
    height: 316px;
    background: var(--paper);
    overflow: hidden;
    box-shadow: 0 2px 6px rgba(0,0,0,0.12);
  }
  .card--first { left: 106px; }
  .card--third { left: 644px; }
  .card__photo { position: absolute; inset: 0; width: 443px; height: 316px; }
  .card__block { position: absolute; white-space: nowrap; }

  .title-lead {
    left: 21px; top: 10px;
    color: var(--rust); font-weight: 600; font-size: 19.5px; line-height: 25.5px;
    letter-spacing: 0.1px;
  }
  .intro { font-size: 7.6px; line-height: 9.5px; }
  .card--first .intro { left: 25px; top: 64px; }
  .subhead {
    left: 25px; top: 118px; color: var(--rust);
    font-weight: 600; font-size: 13.5px; letter-spacing: 0.3px;
  }
  .checklist { left: 26px; top: 140px; list-style: none; font-size: 7.6px; }
  .checklist li { display: flex; align-items: center; height: 13.7px; }
  .checklist .box {
    width: 7px; height: 7px; border: 0.8px solid var(--navy);
    margin-right: 7px; flex: none;
  }
  .checklist .note { display: block; padding-left: 14px; line-height: 9.3px; height: auto; margin-top: 2px; }
  .closing { font-size: 7.6px; line-height: 9.5px; }
  .card--first .closing { left: 21px; top: 242px; }
  .divider { height: 0.8px; background: var(--rule); }
  .card--first .divider { left: 21px; top: 278px; width: 290px; }
  .signer { left: 22px; top: 283px; font-size: 8.8px; font-weight: 600; }
  .signer .cred, .company .cred, .web .accent { color: var(--rust); }
  .contact-line { left: 22px; top: 297px; font-size: 6.2px; }
  .contact-line b { font-weight: 600; }

  .title-plain {
    left: 22px; top: 38px;
    font-size: 12.3px; line-height: 14.6px; font-weight: 400; letter-spacing: 0.2px;
  }
  .card--third .intro { left: 22px; top: 74px; }
  .prompt { left: 22px; top: 136px; font-size: 7.4px; }
  .questions { left: 22px; top: 155px; font-size: 7.6px; line-height: 9.5px; list-style: none; }
  .questions li { margin-bottom: 9.5px; }
  .card--third .closing { left: 22px; top: 232px; }
  .card--third .divider { left: 22px; top: 281px; width: 262px; }
  .company { left: 22px; top: 287px; font-size: 6.8px; font-weight: 600; }
  .address { left: 22px; top: 296px; font-size: 6.8px; }
</style>
</head>
<body>

<section class="card card--first">
  <svg class="card__photo" viewBox="0 0 443 316" role="img" aria-label="Photo of stacked orange and steel-blue chevron sculpture">
    <defs>
      <linearGradient id="photoFirst" x1="0" y1="0" x2="1" y2="1">
        <stop offset="0" stop-color="var(--photo-orange)"/>
        <stop offset="0.45" stop-color="var(--photo-blue)"/>
        <stop offset="1" stop-color="var(--photo-steel)"/>
      </linearGradient>
    </defs>
    <polygon points="375,0 443,0 443,316 290,316" fill="url(#photoFirst)"/>
  </svg>

  <h1 class="card__block title-lead">IS A FIRST-PARTY SPECIAL NEEDS<br>TRUST RIGHT FOR YOU?</h1>
  <p class="card__block intro">Do you have a recognized disability by the social security Administration<br>that renders you unable to engage in any substantial gainful activity by<br>reason of any medically determined physical or mental impairment which<br>can be expected to result in death or which has lasted or can be expected to<br>last for a continuous period of not less than twelve months?</p>
  <h2 class="card__block subhead">ARE YOU...</h2>
  <ul class="card__block checklist">
    <li><span class="box"></span>Under age 65?</li>
    <li><span class="box"></span>Expecting settlement proceeds from the negligent actions of a third party?</li>
    <li><span class="box"></span>Expecting an inheritance?</li>
    <li><span class="box"></span>Currently receiving, or will be applying for Social Security income?</li>
    <li><span class="box"></span>Currently receiving, or will be applying for Medicaid?</li>
    <li class="note">Wanting to maintain or qualify for Social Security<br>Income and/or medicaid after being awarded your<br>settlement or inheritance?</li>
  </ul>
  <p class="card__block closing">If you have a recognized disability and you answered yes to any of<br>these questions, you should contact our office to discuss whether a<br>First-party Special Needs Trust is right for you.</p>
  <div class="card__block divider"></div>
  <p class="card__block signer">Dorian Maskell, <span class="cred">JD</span></p>
  <p class="card__block contact-line"><b>P:</b> (435) 555-0172 &nbsp;| <b>E:</b> hello@truemark-example.com | <b class="web">www.<span class="accent">truemark-example</span>.com</b></p>
</section>

<section class="card card--third">
  <svg class="card__photo" viewBox="0 0 443 316" role="img" aria-label="Photo of nested orange and blue square sculpture lit from behind">
    <defs>
      <linearGradient id="photoThird" x1="0" y1="0" x2="1" y2="1">
        <stop offset="0" stop-color="var(--photo-blue)"/>
        <stop offset="0.5" stop-color="var(--photo-orange)"/>
        <stop offset="1" stop-color="var(--photo-steel)"/>
      </linearGradient>
    </defs>
    <polygon points="352,0 443,0 443,316 280,316" fill="url(#photoThird)"/>
  </svg>

  <h1 class="card__block title-plain">IS A THIRD-PARTY SUPPLEMENTAL NEEDS TRUST<br>NECESSARY FOR YOUR ESTATE PLAN?</h1>
  <p class="card__block intro">Will one of your intended beneficiaries have a recognized disabillity as<br>determined by the Social Security Administration that renders the beneficiary<br>unable to engage in any substantial gainful activity by reason of any<br>medically determined physical or mental impairment which can be expected<br>to result in death or which has lasted or van be expected to last for a<br>continuous period of not less than twelve months?</p>
  <p class="card__block prompt">DOES THE INTENDED BENEFICIARY...</p>
  <ul class="card__block questions">
    <li>Currently receive or will be applying for Social Security income?</li>
    <li>Currently receive, or plan to apply for Medicaid?</li>
    <li>Want to maintain or qualify for Social Security income and/or<br>medicaid after benefitting from an inheritance?</li>
  </ul>
  <p class="card__block closing">If you have an intended beneficiary with a recognized disabillity and<br>you answered yes to any of these questions, you should contact our<br>office to discuss whether a Third-Party Supplemental NeedsTrust is<br>right for your estate plan.</p>
  <div class="card__block divider"></div>
  <p class="card__block company">TrueMark, <span class="cred">PLLC</span></p>
  <p class="card__block address">538 E. Harlow Ave, Ste. 410, St. George, UT 84913</p>
</section>

</body>
</html>
```